design double sided business cards - MOVE WIDE

Mr. Talor
Creative Director
318-742-000

IG MoveWide
movewidewear@mailnest.com
www.movewide47.com

***FINAL FILES MUST BE 300DPI CMYK LAYERED PSD FILES WITH EDITABLE TEXT***
**SIZE IS US STANDARD 2X3.5 WITH AN EXTRA 0.125 ADDED TO WIDTH AND LENGTH FOR BLEED**

Design should be very creative, design should represent excitement, creativity

```html
<!DOCTYPE html>
<html lang="en">
<head>
<meta charset="utf-8">
<title>MOVE WIDE – Business Card, Front and Back</title>
<link rel="stylesheet" href="https://fonts.googleapis.com/css2?family=Montserrat:wght@400;600;800&display=swap">
<style>
  :root {
    --backdrop: #e4e5e8;
    --card: #ffffff;
    --red: #e5161b;
    --black: #141414;
    --ink: #1d1d1d;
    --ink-soft: #4a4a4a;
  }
  html, body {
    margin: 0;
    padding: 0;
    width: 1200px;
    height: 1200px;
    overflow: hidden;
    background: var(--backdrop);
  }
  .canvas {
    width: 1200px;
    height: 1200px;
    display: flex;
    flex-direction: column;
    align-items: center;
    justify-content: center;
    gap: 56px;
  }
  .business-card {
    position: relative;
    width: 900px;
    height: 514px;
    background: var(--card);
    box-shadow: 0 10px 30px rgba(0,0,0,0.12);
    overflow: hidden;
    font-family: "Montserrat", sans-serif;
  }
  .pattern-band {
    position: absolute;
    left: 0;
    height: 150px;
    background: linear-gradient(90deg, var(--red) 0%, var(--red) 55%, var(--black) 100%);
  }
  /* Front side */
  .card-front .brand-name {
    position: absolute;
    left: 80px;
    top: 90px;
    margin: 0;
    font-size: 56px;
    font-weight: 800;
    letter-spacing: 1px;
    color: var(--red);
    line-height: 1;
  }
  .card-front .pattern-band {
    top: 260px;
    width: 900px;
  }
  /* Back side */
  .card-back .pattern-band {
    top: 182px;
    width: 540px;
  }
  .contact {
    position: absolute;
    left: 590px;
    top: 168px;
    color: var(--ink);
  }
  .contact-name {
    margin: 0 0 4px;
    font-size: 30px;
    font-weight: 600;
  }
  .contact-role {
    margin: 0 0 16px;
    font-size: 16px;
    color: var(--ink-soft);
  }
  .contact-line {
    margin: 0 0 6px;
    font-size: 14px;
    color: var(--ink-soft);
  }
</style>
</head>
<body>
<main class="canvas">
  <section class="business-card card-front">
    <h1 class="brand-name">MOVE WIDE</h1>
    <div class="pattern-band" role="img" aria-label="Red and black angular triangle pattern band"></div>
  </section>

  <section class="business-card card-back">
    <div class="pattern-band" role="img" aria-label="Red and black angular triangle pattern band"></div>
    <div class="contact">
      <p class="contact-name">Mr. Talor</p>
      <p class="contact-role">Creative Director</p>
      <p class="contact-line">Tel: 318-742-000</p>
      <p class="contact-line">IG: MoveWide</p>
      <p class="contact-line">movewidewear@mailnest.com</p>
      <p class="contact-line">www.movewide47.com</p>
    </div>
  </section>
</main>
</body>
</html>
```